Web Design Project

New website for Aged Care business.

Easy buttons to

1.book appointment

2.request a callback

3.view services

think elderly people using it, or family members

we like the colours of 'tidewell' website

and the middle image and call to action buttons of the rons edging website.

we'd like a rotating image similar to the rons edging but bigger size.

http://www.tidewell.org.au/

http://www.ronsedging.net/

Reason: need to have a meeting with our staff to decide - i'm overseas..

Target Market(s)

elderly people and families of elderly people with enough money to pay for the services offered.

Industry/Entity Type

Business

Requirements
Must have
• contemporary and clean design

```html
<!DOCTYPE html>
<html lang="en">
<head>
<meta charset="utf-8">
<title>Everhaven – Home</title>
<link href="https://fonts.googleapis.com/css2?family=Open+Sans:wght@400;600;700&display=swap" rel="stylesheet">
<style>
  :root{
    --sky:#3aa3dc;
    --sky-pale:#e4f2fb;
    --navy:#1f4f7d;
    --text:#5b6670;
    --muted:#8a949c;
    --page:#f1f3f5;
    --white:#ffffff;
    --green:#6fb53c;
    --line:#d7dde2;
  }
  *{box-sizing:border-box;margin:0;padding:0}
  html,body{width:820px;height:1200px;overflow:hidden}
  body{background:var(--page);font-family:"Open Sans",Arial,sans-serif;color:var(--text);font-size:10px;line-height:1.45}
  .site-header{height:68px;background:linear-gradient(#f7fbfe,var(--sky-pale))}
  .header-inner{width:700px;margin:0 auto;height:68px;display:flex;align-items:center;justify-content:space-between}
  .brand{display:flex;align-items:center;gap:8px;font-size:26px;font-weight:600;color:var(--sky)}
  .brand-dot{width:14px;height:14px;border-radius:50%;background:var(--sky)}
  .header-contact{text-align:right}
  .phone{display:flex;align-items:center;gap:6px;font-size:22px;font-weight:700;color:var(--sky)}
  .social{display:flex;gap:5px;justify-content:flex-end;margin-top:4px}
  .social span{width:14px;height:14px;border-radius:50%;background:var(--navy)}
  .main-nav{width:700px;margin:0 auto;height:30px;background:var(--navy);display:flex;border-radius:3px 3px 0 0}
  .main-nav a{color:var(--white);text-decoration:none;font-size:9px;font-weight:600;padding:0 17px;line-height:30px;text-transform:uppercase}
  .main-nav a.active{background:var(--sky)}
  .page{width:700px;margin:0 auto;background:var(--white);padding:14px 20px 20px}
  .slider{height:290px;border:5px solid var(--white);box-shadow:0 0 0 1px var(--line);border-radius:4px;background:linear-gradient(135deg,#c9b9a2,#e6d9c6 45%,#8fb6d6)}
  .slider-dots{display:flex;justify-content:center;gap:5px;margin:7px 0 14px}
  .slider-dots span{width:6px;height:6px;border-radius:50%;background:var(--line)}
  .slider-dots span.on{background:var(--sky)}
  .content{display:flex;gap:22px}
  .welcome{flex:1}
  .welcome h1{font-size:27px;font-weight:400;color:var(--sky);margin-bottom:10px}
  .welcome p{margin-bottom:9px}
  .welcome h2{font-size:10px;font-weight:700;color:#444;margin:4px 0 6px}
  .learn-more{display:block;text-align:right;color:var(--navy);font-weight:700;font-size:9px;text-decoration:none}
  .booking{width:190px;background:var(--sky-pale);border:1px solid #bcdcf0;border-radius:6px;padding:0 12px 14px}
  .booking h3{background:var(--sky);color:var(--white);font-size:13px;font-weight:600;text-align:center;margin:0 -12px 10px;padding:8px 0;border-radius:5px 5px 0 0}
  .booking label{display:block;font-size:9px;font-weight:600;color:var(--navy);margin:8px 0 3px}
  .field{height:20px;background:var(--white);border:1px solid #c2d6e4;border-radius:3px}
  .field.tall{height:46px}
  .date-row{display:flex;gap:4px}
  .date-row .field{flex:1}
  .book-btn{display:block;margin:14px auto 0;width:110px;height:26px;border-radius:13px;background:var(--sky);color:var(--white);font-size:10px;font-weight:700;text-align:center;line-height:26px}
  .features{width:700px;margin:12px auto 0;background:var(--white);padding:16px 20px;display:grid;grid-template-columns:repeat(4,1fr);gap:14px}
  .feature-img{height:48px;border-radius:4px;margin-bottom:6px}
  .feature h4{font-size:11px;color:var(--navy);font-weight:700;margin-bottom:4px}
  .feature p,.feature li{font-size:8px;color:var(--muted)}
  .feature ul{padding-left:10px}
  .view-more{font-size:8px;font-weight:700;color:var(--navy);display:block;margin-top:5px}
  .callback h4{color:var(--green)}
  .site-footer{margin-top:20px;height:210px;background:linear-gradient(#dbeefa,#c7e4f6)}
  .footer-inner{width:700px;margin:0 auto;padding-top:30px;display:flex;align-items:flex-start;gap:40px}
  .footer-brand{width:170px;display:flex;align-items:center;gap:8px;margin-top:36px;font-size:24px;font-weight:600;color:var(--sky)}
  .footer-links{flex:1;background:var(--white);border-radius:10px;padding:12px 20px;display:flex;gap:40px}
  .footer-links ul{list-style:none}
  .footer-links li{font-size:9px;color:var(--text);line-height:16px}
  .footer-links li::before{content:"•";color:var(--sky);margin-right:5px}
  .copyright{width:700px;margin:30px auto 0;text-align:right;font-size:8px;color:var(--muted)}
</style>
</head>
<body>
<header class="site-header">
  <div class="header-inner">
    <div class="brand"><span class="brand-dot"></span>Everhaven</div>
    <div class="header-contact">
      <div class="phone">
        <svg width="18" height="18" viewBox="0 0 24 24" aria-hidden="true"><path fill="#3aa3dc" d="M6.6 10.8a15.1 15.1 0 0 0 6.6 6.6l2.2-2.2a1 1 0 0 1 1-.25 11.4 11.4 0 0 0 3.6.57 1 1 0 0 1 1 1V20a1 1 0 0 1-1 1A17 17 0 0 1 3 4a1 1 0 0 1 1-1h3.5a1 1 0 0 1 1 1c0 1.25.2 2.45.57 3.6a1 1 0 0 1-.25 1z"/></svg>
        1800-55-0192
      </div>
      <div class="social"><span></span><span></span></div>
    </div>
  </div>
</header>

<nav class="main-nav">
  <a class="active" href="#">Home</a>
  <a href="#">About Us</a>
  <a href="#">Our Services</a>
  <a href="#">Care &amp; Support</a>
  <a href="#">Book an Appointment</a>
  <a href="#">Contact Us</a>
</nav>

<main class="page">
  <div class="slider" role="img" aria-label="Rotating banner photo of a smiling elderly couple outdoors"></div>
  <div class="slider-dots"><span class="on"></span><span></span><span></span></div>

  <div class="content">
    <section class="welcome">
      <h1>Welcome come to Everhaven</h1>
      <p>We support older people to live well, safely and with dignity, whether at home or in one of our caring residences. Our trained staff work closely with families to shape a plan that suits each person.</p>
      <p>Every plan begins with a friendly chat. We listen to what matters most, from daily routines and meals to hobbies, visitors and health needs, then build support around them.</p>
      <p>Nurses, carers and allied health staff are on hand every day, and families can call us at any time for an update or to ask a question.</p>
      <p>Our homes are light, calm and close to shops, parks and transport, so residents stay part of the local community they know and love.</p>
      <h2>What we offer:</h2>
      <p>Home visits, respite stays, dementia care, meals, transport and social outings can be combined as needed. Services can change as needs change, with no long waiting lists and a single contact person for your family.</p>
      <p>Book a visit to meet our team, see our rooms and gardens, and share a cup of tea. We are happy to help you compare options.</p>
      <a class="learn-more" href="#">Learn more</a>
    </section>

    <aside class="booking">
      <h3>Book An Appointment</h3>
      <label>Preferred Date &amp; Time:</label>
      <div class="date-row"><div class="field"></div><div class="field"></div><div class="field"></div></div>
      <label>Your Name:</label><div class="field"></div>
      <label>Email:</label><div class="field"></div>
      <label>Address:</label><div class="field tall"></div>
      <label>Phone:</label><div class="field"></div>
      <span class="book-btn">BOOK NOW</span>
    </aside>
  </div>
</main>

<section class="features">
  <div class="feature">
    <div class="feature-img" role="img" aria-label="Photo of a carer holding an elderly person's hands" style="background:linear-gradient(135deg,#6fa9d4,#cfe3f2)"></div>
    <h4>Care &amp; Support</h4>
    <p>Personal care, nursing and daily help delivered with patience and respect, at home or in residence.</p>
    <a class="view-more">View More</a>
  </div>
  <div class="feature">
    <div class="feature-img" role="img" aria-label="Photo of a smiling senior woman" style="background:linear-gradient(135deg,#d8c3a8,#f1e6d6)"></div>
    <h4>Why Choose Everhaven?</h4>
    <p>Local, family minded and trusted for years, we put comfort, choice and peace of mind first.</p>
    <a class="view-more">View More</a>
  </div>
  <div class="feature">
    <div class="feature-img" role="img" aria-label="Photo of seniors enjoying an activity together" style="background:linear-gradient(135deg,#a7b7c4,#e2e8ed)"></div>
    <h4>Our Service Range</h4>
    <ul><li>Home care visits</li><li>Respite stays</li><li>Dementia support</li><li>Meals and transport</li></ul>
    <a class="view-more">View More</a>
  </div>
  <div class="feature callback">
    <div class="feature-img" role="img" aria-label="Image of a telephone for call back requests" style="background:linear-gradient(135deg,#8cc75c,#d8edc6)"></div>
    <h4>Request A Call Back</h4>
    <p>Leave your number and one of our friendly team will call you back at a time that suits.</p>
    <a class="view-more">View More</a>
  </div>
</section>

<footer class="site-footer">
  <div class="footer-inner">
    <div class="footer-brand"><span class="brand-dot"></span>Everhaven</div>
    <div class="footer-links">
      <ul><li>Care &amp; Support</li><li>Our History</li><li>Mission and values</li><li>Why Everhaven?</li><li>Research</li></ul>
      <ul><li>Careers</li><li>Volunteers</li><li>Donate</li><li>Referrals</li></ul>
      <ul><li>Site Map</li><li>Privacy Policy</li><li>Legal Statement</li></ul>
    </div>
  </div>
  <p class="copyright">© Everhaven 2024. All rights reserved.</p>
</footer>
</body>
</html>
```